Email Preference Page Design

We are looking for a 2 page design for our users to edit their email preferences and submit friend referrals. You can find the fuctionality, content and text here:

https://brightreel.mailvector.example/app/linkClick/7281/5b9c1d04e6a7f318/20583147/8d4f2a61c0b9e357

* the shipping and billing address might be different so you need to show the billing if the "same as shipping" box is not checked. It can auto-hide like the page above shows if that fits your design.

* when the "unsubscribe from all email lists" box is selected, all the other checkbox options will hide as in the example page. We need you to show us what the site will look like with and without that checkbox selected.

We want to match these two pages to the general feel of these website pages:

www.brightreel.example
and
free.brightreel.example

The page should be very clean and tight. Project is for design only but must be able to be implemented in html showing button and checkbox states. Technically this must be two pages for our system - one for all the user info and one for individual email referrals (see example above).

Target Market(s)

video professionals

Industry/Entity Type

Shipping

Requirements
Must have
• our logo (see numerous versions attached)
well designed header
well designed sections
clean editable text
tight layout
html friendly
easy to understand
2 pages
Nice to have
• custom checkboxes and radio buttons

```html
<!DOCTYPE html>
<html lang="en">
<head>
<meta charset="utf-8">
<title>Communication Preferences – BrightReel</title>
<link href="https://fonts.googleapis.com/css2?family=Ropa+Sans&family=PT+Sans:wght@400;700&display=swap" rel="stylesheet">
<style>
:root{
  --ink:#2f2f2f;
  --navy:#1d2a36;
  --navy-line:#31404d;
  --tab:#3b3b3b;
  --orange:#e9541d;
  --orange-soft:#f3a25a;
  --paper:#f6f6f6;
  --field:#ffffff;
  --field-edge:#dcdcdc;
  --muted:#8a96a0;
  --footer-text:#d9dee2;
}
*{box-sizing:border-box;margin:0;padding:0}
html,body{width:690px;height:1200px;overflow:hidden}
body{position:relative;background:var(--paper);font-family:"PT Sans",sans-serif;color:var(--ink)}
.abs{position:absolute}
.topbar{left:0;top:0;width:690px;height:35px;background:var(--navy);border-bottom:1px solid var(--navy-line);display:flex;align-items:center;justify-content:center;gap:6px}
.brand-dot{width:11px;height:11px;border-radius:50%;background:var(--orange)}
.brand-name{font-family:"PT Sans",sans-serif;font-size:17px;color:#fff}
.hero{left:0;top:36px;width:690px;height:126px;background:linear-gradient(100deg,#5b3a2a 0%,#2c3a5c 25%,#4a4f7a 45%,#6a4e5a 65%,#b6a5a8 85%,#7c6a70 100%)}
.page-title{left:206px;top:142px;width:280px;height:32px;background:var(--paper);text-align:center;font-family:"Ropa Sans",sans-serif;font-size:25px;line-height:32px;color:var(--orange)}
.section-head{height:28px;border-bottom:2px solid var(--tab)}
.section-head span{display:inline-block;height:28px;padding:0 7px;background:var(--tab);color:#fff;font-family:"Ropa Sans",sans-serif;font-size:18px;line-height:28px}
.field-label{width:150px;text-align:right;font-size:10px;line-height:24px}
.field-label em{color:var(--orange);font-style:normal}
.field{height:24px;background:var(--field);border:1px solid var(--field-edge);border-bottom-width:3px;border-radius:2px}
.select-arrow{position:absolute;right:8px;top:8px;width:0;height:0;border-left:4px solid transparent;border-right:4px solid transparent;border-top:5px solid #b9b9b9}
.plus{left:238px;top:592px;font-size:10px;color:#aaa;line-height:24px}
.check{width:14px;height:14px}
.opt{font-size:8.5px;line-height:14px}
.subscribe{left:57px;top:641px;width:575px;height:33px;background:var(--tab);border-radius:2px;display:flex;align-items:center;padding-left:26px;gap:6px}
.subscribe strong{font-family:"Ropa Sans",sans-serif;font-weight:400;font-size:15px;color:#fff;margin-right:10px}
.subscribe small{font-size:9.5px;color:#e8e8e8}
.filter-title{left:0;width:690px;top:709px;text-align:center;font-family:"Ropa Sans",sans-serif;font-size:15px}
.group-box{top:739px;height:31px;border:1px solid #bbb;background:#fff;text-align:center;font-size:10px;line-height:29px}
.unsub{color:var(--orange)}
.submit{left:303px;top:1043px;width:83px;height:31px;background:var(--orange);border:1px solid #d0461a;border-radius:2px;color:#fff;font-family:"Ropa Sans",sans-serif;font-size:17px;text-align:center;line-height:29px}
.footer{left:0;top:1101px;width:690px;height:99px;background:var(--navy)}
.footer-links{top:1127px;left:0;width:690px;text-align:center;font-size:7.5px;color:var(--footer-text)}
.footer-links span+span::before{content:"·";color:var(--muted);margin:0 4px}
.copyright{top:1142px;left:0;width:690px;text-align:center;font-size:7.5px;color:var(--footer-text)}
.social{top:1160px;left:316px;display:flex;gap:2px}
.social i{display:block;width:18px;height:18px;border-radius:50%;border:1px solid #b08a3a}
</style>
</head>
<body>
<svg width="0" height="0" style="position:absolute">
  <defs>
    <symbol id="box" viewBox="0 0 14 14"><rect x="0.75" y="0.75" width="12.5" height="12.5" rx="2" fill="#fff" stroke="#f3a25a" stroke-width="1.2"/></symbol>
    <symbol id="box-on" viewBox="0 0 14 14"><rect x="0.75" y="0.75" width="12.5" height="12.5" rx="2" fill="#fff" stroke="#f3a25a" stroke-width="1.2"/><path d="M3.8 7.2l2.2 2.2 4.4-4.8" fill="none" stroke="#e9541d" stroke-width="1.4"/></symbol>
  </defs>
</svg>

<header class="abs topbar"><i class="brand-dot"></i><span class="brand-name">brightreel</span></header>
<div class="abs hero" role="img" aria-label="Blurred photo of neon city lights at night"></div>
<h1 class="abs page-title">Communication Preferences</h1>

<div class="abs section-head" style="left:58px;top:194px;width:268px"><span>Contact Info</span></div>
<div class="abs section-head" style="left:363px;top:194px;width:269px"><span>Shipping Info</span></div>

<label class="abs field-label" style="left:0;top:243px">First Name<em>*</em></label><div class="abs field" style="left:164px;top:243px;width:146px"></div>
<label class="abs field-label" style="left:0;top:278px">Last Name<em>*</em></label><div class="abs field" style="left:164px;top:278px;width:146px"></div>
<label class="abs field-label" style="left:0;top:312px">E-mail<em>*</em></label><div class="abs field" style="left:164px;top:312px;width:146px"></div>
<label class="abs field-label" style="left:0;top:347px">Phone</label><div class="abs field" style="left:164px;top:347px;width:146px"></div>
<label class="abs field-label" style="left:0;top:382px">Address 1</label><div class="abs field" style="left:164px;top:382px;width:146px"></div>
<label class="abs field-label" style="left:0;top:417px">Address 2</label><div class="abs field" style="left:164px;top:417px;width:146px"></div>
<label class="abs field-label" style="left:0;top:451px">Address 3</label><div class="abs field" style="left:164px;top:451px;width:146px"></div>
<label class="abs field-label" style="left:0;top:486px">City</label><div class="abs field" style="left:164px;top:486px;width:146px"></div>
<label class="abs field-label" style="left:0;top:521px">Country</label><div class="abs field" style="left:164px;top:521px;width:146px"><i class="select-arrow"></i></div>
<label class="abs field-label" style="left:0;top:555px">State</label><div class="abs field" style="left:164px;top:555px;width:146px"></div>
<label class="abs field-label" style="left:0;top:590px">Postal Code + 4</label><div class="abs field" style="left:164px;top:590px;width:69px"></div>
<span class="abs plus">+</span><div class="abs field" style="left:254px;top:590px;width:56px"></div>

<svg class="abs check" style="left:370px;top:248px"><use href="#box-on"/></svg>
<span class="abs opt" style="left:391px;top:248px;font-size:9.5px">Billing address is same as shipping address</span>

<div class="abs subscribe">
  <svg class="check"><use href="#box-on"/></svg>
  <strong>Subscribe me to your general email list</strong>
  <small>This monthly email includes free video loops and VIP sale notices</small>
</div>

<h2 class="abs filter-title">Help us filter our emails so we are only sendiong relevant information to you</h2>
<div class="abs group-box" style="left:58px;width:269px">Send me emails about these product types</div>
<div class="abs group-box" style="left:362px;width:270px">I am Involved in or have interest in</div>

<svg class="abs check" style="left:96px;top:790px"><use href="#box-on"/></svg><span class="abs opt" style="left:118px;top:790px">Low energy motion loops</span>
<svg class="abs check" style="left:96px;top:814px"><use href="#box"/></svg><span class="abs opt" style="left:118px;top:814px">High energy motion loops</span>
<svg class="abs check" style="left:96px;top:838px"><use href="#box"/></svg><span class="abs opt" style="left:118px;top:838px">Timelapse footage</span>
<svg class="abs check" style="left:96px;top:862px"><use href="#box"/></svg><span class="abs opt" style="left:118px;top:862px">Worship or wedding motion loops</span>
<svg class="abs check" style="left:96px;top:886px"><use href="#box"/></svg><span class="abs opt" style="left:118px;top:886px">Pre-mixed DVDs and BluRay</span>
<svg class="abs check" style="left:96px;top:910px"><use href="#box"/></svg><span class="abs opt" style="left:118px;top:910px">Entertainment lasers for concerts and clubs</span>
<svg class="abs check" style="left:96px;top:934px"><use href="#box"/></svg><span class="abs opt" style="left:118px;top:934px">Entertainment lasers for text &amp; logo display</span>
<svg class="abs check" style="left:96px;top:958px"><use href="#box"/></svg><span class="abs opt" style="left:118px;top:958px">Custom logo animation services</span>
<svg class="abs check" style="left:96px;top:982px"><use href="#box"/></svg><span class="abs opt" style="left:118px;top:982px">Video software for creating video animations</span>
<svg class="abs check" style="left:96px;top:1006px"><use href="#box"/></svg><span class="abs opt" style="left:118px;top:1006px">Video software for live performance (Vjing)</span>

<svg class="abs check" style="left:400px;top:790px"><use href="#box-on"/></svg><span class="abs opt" style="left:423px;top:790px">VJing (live performance video)</span>
<svg class="abs check" style="left:400px;top:814px"><use href="#box"/></svg><span class="abs opt" style="left:423px;top:814px">DJing (live performance audio+video)</span>
<svg class="abs check" style="left:400px;top:838px"><use href="#box"/></svg><span class="abs opt" style="left:423px;top:838px">Performing in a band</span>
<svg class="abs check" style="left:400px;top:862px"><use href="#box"/></svg><span class="abs opt" style="left:423px;top:862px">Video editing</span>
<svg class="abs check" style="left:400px;top:886px"><use href="#box"/></svg><span class="abs opt" style="left:423px;top:886px">Corporate presentations</span>
<svg class="abs check" style="left:400px;top:910px"><use href="#box"/></svg><span class="abs opt" style="left:423px;top:910px">Worship video services</span>
<svg class="abs check" style="left:400px;top:934px"><use href="#box"/></svg><span class="abs opt" style="left:423px;top:934px">Lasers for entertainment &amp; branding</span>
<svg class="abs check" style="left:400px;top:958px"><use href="#box"/></svg><span class="abs opt" style="left:423px;top:958px">Special offers from BrightReel partners</span>
<svg class="abs check" style="left:400px;top:1006px"><use href="#box"/></svg><span class="abs opt unsub" style="left:423px;top:1006px">Unsubscribe from all email lists</span>

<div class="abs submit">SUBMIT</div>

<footer class="abs footer"></footer>
<nav class="abs footer-links"><span>Free Videos</span><span>BrightReel</span><span>Swift Video</span><span>Free Sign-Up</span><span>About Us</span><span>Contact Us</span></nav>
<p class="abs copyright">All Rights Reserved Copyright© 2013 - BrightReel</p>
<div class="abs social"><i></i><i></i><i></i></div>
</body>
</html>
```